Responsive Website Design for New Social Site (Building User Account)

Brellomar.com is a website that allows people to create preformatted emails to be sent out at a later date. The purpose is to allow people to communicate in the event of an accident or death. The beta site is built but not consumable by the public. It needs a new look before we go live.

I’m speaking specifically about the user account. They are admin tools for creating and publishing communications. They include workflow design, document/message storage, and a dashboard.

I currently have a basic design. Now I’m looking for an inspired design. Something interesting and memorable. Something that draws people in. I have a PPT that can provide guidance on what elements need to be on each page but I’m looking for someone who knows how to create engaging websites.

SCOPE OF EFFORT
There are approximately 23 pages to the website but only 5 distinct page appearances
• Dashboard
• Workflow
• Document/Message/Contact Management
• Education Search
• Account Form
I need a few pop-up designs
• Yes/No/Continue
I need a responsive design (3 sizes)

ARTISTIC QUALITIES
Easy to Use/Understand
New/Inventive/Cool/Memorable
Works with the Logo
Consistent Elements (buttons, text, use of color, etc)

TECHNICAL ASPECTS
I’d like the work provided in a storyboard and individual files for development

PHASES
1. Initial Concept
a. 2-3 Designs Ideas. Just the Dashboard and Workflow in responsive formats
2. Build
a. Create all the pages
b. Provide in storyboard in responsive formats
c. 2 Rounds of Revision
3. Final
a. Provide Storyboard and Files

I'd like to see a portfolio of your responsive web design, especially any user accounts you have created. I've attached three of the initial pages. I'd like to see a concept of what you would produce for at least one of the pages.

Thank you for your interest.

```html
<!DOCTYPE html>
<html lang="en">
<head>
<meta charset="utf-8">
<title>Brellomar – Learning Center</title>
<link href="https://fonts.googleapis.com/css2?family=Lato:ital,wght@0,300;0,400;0,700;1,400&display=swap" rel="stylesheet">
<style>
:root{
  --blue:#2b9be0;
  --blue-dark:#1f86c9;
  --sidebar:#30313a;
  --sidebar-row:#373842;
  --line:#3e3f4a;
  --page:#f0f0f0;
  --ink:#333;
  --muted:#555;
  --purple:#5b3fb0;
  --magenta:#a000b0;
  --green:#12a012;
  --teal:#0e9aab;
  --orange:#e88a12;
  --sky:#2d9de0;
  --red:#ee4a24;
  --lime:#8bbb3d;
  --footer:#232325;
}
*{box-sizing:border-box;margin:0;padding:0}
html,body{width:1161px;height:1200px;overflow:hidden}
body{font-family:'Lato',sans-serif;background:var(--page);color:var(--ink);position:relative}
.topbar{position:absolute;left:0;top:0;width:1161px;height:91px;background:#fff;border-bottom:1px solid #e2e2e2}
.brand{position:absolute;left:23px;top:26px;display:flex;align-items:center;gap:10px}
.brand-dot{width:40px;height:40px;border-radius:50%;background:var(--blue)}
.brand-name{font-size:25px;font-weight:700;color:var(--blue);line-height:1}
.brand-tag{font-size:8.5px;color:#555;margin-top:4px}
.topbar .divider{position:absolute;left:1090px;top:16px;width:1px;height:50px;background:#eee}
.icon-btn{position:absolute;top:33px}
.sidebar{position:absolute;left:0;top:91px;width:260px;height:1044px;background:var(--sidebar)}
.avatar{position:absolute;left:74px;top:28px;width:96px;height:96px;border-radius:50%;border:3px solid #fff;background:radial-gradient(circle at 50% 40%,#c9cdd4,#4a5466)}
.user-name{position:absolute;top:133px;width:100%;text-align:center;color:#fff;font-size:20px}
.user-role{position:absolute;top:155px;width:100%;text-align:center;color:#ddd;font-size:12.5px;font-style:italic}
.nav{position:absolute;top:190px;left:0;width:260px;list-style:none}
.nav li{height:53px;display:flex;align-items:center;border-bottom:1px solid var(--line);background:var(--sidebar-row)}
.nav .ico{width:66px;height:53px;display:flex;align-items:center;justify-content:center}
.nav .label{flex:1;color:#fff;font-size:16.5px;padding-left:13px}
.nav .chev{margin-right:20px}
.main-title{position:absolute;left:260px;width:885px;top:116px;text-align:center;font-size:25px;font-weight:400;color:#333}
.quicklinks{position:absolute;left:293px;top:162px;width:839px;height:92px;background:#fff;border:1px solid #e3e3e3}
.qbtn{position:absolute;top:24px;height:43px;background:linear-gradient(#33a3e6,var(--blue-dark));color:#fff;font-size:20px;display:flex;align-items:center;justify-content:center;border-radius:2px}
.tile{position:absolute;top:289px;width:199px;height:149px;color:#fff;overflow:hidden}
.tile::before{content:"";position:absolute;left:60px;top:-40px;width:160px;height:160px;background:rgba(255,255,255,.07);transform:rotate(45deg)}
.tile .ring{position:absolute;left:65px;top:24px;width:68px;height:68px;border:1.5px solid #fff;border-radius:50%;display:flex;align-items:center;justify-content:center}
.tile .badge{position:absolute;left:115px;top:10px;width:29px;height:29px;border-radius:50%;background:#fff;font-size:14px;display:flex;align-items:center;justify-content:center}
.tile .name{position:absolute;top:110px;width:100%;text-align:center;font-size:16px}
.section-title{position:absolute;left:260px;width:906px;top:490px;text-align:center;font-size:25px;color:#333}
.plan{position:absolute;top:553px;width:100px;text-align:center}
.plan .circ{width:100px;height:100px;border:1px solid var(--blue);border-radius:50%;display:flex;align-items:center;justify-content:center}
.plan .cap{margin-top:13px;font-size:17.5px;color:#444;margin-left:-20px;margin-right:-20px}
.panel{position:absolute;left:293px;top:729px;width:839px;height:352px;background:#fff;border:1px solid #e3e3e3}
.panel-head{height:44px;background:#fafafa;border-bottom:1px solid #e6e6e6;position:relative}
.panel-head h2{position:absolute;left:16px;top:11px;font-size:18px;font-weight:400;color:var(--blue);letter-spacing:1.2px}
.panel-head .close{position:absolute;right:14px;top:10px;font-size:20px;color:#999}
.row{position:relative;border-bottom:1px solid #ececec}
.row:last-child{border-bottom:none}
.row .title{position:absolute;left:72px;font-size:15px;letter-spacing:1px;color:#444}
.row .meta{position:absolute;left:72px;font-size:12.5px;letter-spacing:.9px;color:#444;word-spacing:2px}
.row .meta span{margin-right:9px}
.row.live .title,.row.live .meta{color:var(--red)}
.tag{position:absolute;left:21px;width:42px;height:35px;border-radius:3px;color:#fff;display:flex;align-items:center;justify-content:center}
.footer{position:absolute;left:0;top:1135px;width:1161px;height:65px;background:var(--footer);color:#fff}
.footer p{position:absolute;width:100%;top:24px;text-align:center;font-size:12px}
.footer .code{position:absolute;left:1104px;top:31px;font-size:12px}
</style>
</head>
<body>
<header class="topbar">
  <div class="brand">
    <div class="brand-dot"></div>
    <div><div class="brand-name">Brellomar</div><div class="brand-tag">The most trusted resource for life management</div></div>
  </div>
  <svg class="icon-btn" style="left:1050px" width="21" height="17" viewBox="0 0 21 17"><path d="M0 1.5h21M0 8.5h21M0 15.5h21" stroke="#666" stroke-width="2"/></svg>
  <div class="divider"></div>
  <svg class="icon-btn" style="left:1107px;top:33px" width="19" height="19" viewBox="0 0 19 19"><circle cx="7.5" cy="7.5" r="6.5" fill="none" stroke="#666" stroke-width="1.8"/><path d="M12.5 12.5l6 6" stroke="#666" stroke-width="1.8"/></svg>
</header>

<aside class="sidebar">
  <div class="avatar" role="img" aria-label="Profile photo of the account holder"></div>
  <div class="user-name">Daniel Rowe</div>
  <div class="user-role">Administrator</div>
  <ul class="nav">
    <li><span class="ico" style="background:var(--purple)"><svg width="20" height="18" viewBox="0 0 20 18"><path d="M10 1L1 9h3v8h4v-5h4v5h4V9h3z" fill="#fff"/></svg></span><span class="label">Home</span><svg class="chev" width="8" height="14"><path d="M1 1l6 6-6 6" stroke="#fff" stroke-width="2" fill="none"/></svg></li>
    <li><span class="ico" style="background:var(--magenta)"><svg width="26" height="24" viewBox="0 0 26 24"><path d="M2 2h8v4a2 2 0 104 0V2h0v8h-4a2 2 0 100 4h4v8H2v-8h4a2 2 0 100-4H2z" fill="#fff"/><rect x="15" y="12" width="9" height="10" fill="#fff"/></svg></span><span class="label">Plans</span><svg class="chev" width="8" height="14"><path d="M1 1l6 6-6 6" stroke="#fff" stroke-width="2" fill="none"/></svg></li>
    <li><span class="ico" style="background:var(--green)"><svg width="20" height="24" viewBox="0 0 20 24"><path d="M1 1h12l6 6v16H1z" fill="none" stroke="#fff" stroke-width="1.6"/><path d="M5 10h10M5 14h10M5 18h10" stroke="#fff" stroke-width="1.4"/></svg></span><span class="label">Documents</span><svg class="chev" width="8" height="14"><path d="M1 1l6 6-6 6" stroke="#fff" stroke-width="2" fill="none"/></svg></li>
    <li><span class="ico" style="background:var(--teal)"><svg width="24" height="22" viewBox="0 0 24 22"><path d="M1 9l11-7 11 7v12H1z M1 9l11 7 11-7" fill="none" stroke="#fff" stroke-width="1.6"/><path d="M6 7h12M6 10h12" stroke="#fff" stroke-width="1.3"/></svg></span><span class="label">Messages</span><svg class="chev" width="8" height="14"><path d="M1 1l6 6-6 6" stroke="#fff" stroke-width="2" fill="none"/></svg></li>
    <li><span class="ico" style="background:var(--orange)"><svg width="26" height="20" viewBox="0 0 26 20"><circle cx="6" cy="6" r="3.5" fill="#fff"/><circle cx="20" cy="6" r="3.5" fill="#fff"/><circle cx="13" cy="8" r="4" fill="#fff"/><path d="M0 17c0-4 3-6 6-6s4 1 4 2M26 17c0-4-3-6-6-6s-4 1-4 2M6 20c0-5 3-8 7-8s7 3 7 8z" fill="#fff"/></svg></span><span class="label">Contact Us</span><svg class="chev" width="8" height="14"><path d="M1 1l6 6-6 6" stroke="#fff" stroke-width="2" fill="none"/></svg></li>
    <li><span class="ico" style="background:var(--sky)"><svg width="18" height="26" viewBox="0 0 18 26"><path d="M9 2a7 7 0 00-4 12.7V19h8v-4.3A7 7 0 009 2z" fill="none" stroke="#fff" stroke-width="1.8"/><path d="M6 22h6M7 25h4" stroke="#fff" stroke-width="1.8"/></svg></span><span class="label">Learning</span><svg class="chev" width="8" height="14"><path d="M1 1l6 6-6 6" stroke="#fff" stroke-width="2" fill="none"/></svg></li>
    <li><span class="ico" style="background:var(--red)"><svg width="24" height="24" viewBox="0 0 24 24"><circle cx="12" cy="12" r="4" fill="none" stroke="#fff" stroke-width="2"/><path d="M3 3l5 5M21 3l-5 5M3 21l5-5M21 21l-5-5" stroke="#fff" stroke-width="2.4"/></svg></span><span class="label">Community</span><svg class="chev" width="8" height="14"><path d="M1 1l6 6-6 6" stroke="#fff" stroke-width="2" fill="none"/></svg></li>
  </ul>
</aside>

<h1 class="main-title">LEARNING CENTER</h1>
<div class="quicklinks">
  <div class="qbtn" style="left:31px;width:209px">Get Started</div>
  <div class="qbtn" style="left:255px;width:209px">Tutorials</div>
  <div class="qbtn" style="left:479px;width:151px">FAQ</div>
  <div class="qbtn" style="left:645px;width:167px">Templates</div>
</div>

<div class="tile" style="left:293px;background:var(--magenta)">
  <div class="ring"><svg width="28" height="28" viewBox="0 0 26 24"><path d="M2 2h8v4a2 2 0 104 0V2h0v8h-4a2 2 0 100 4h4v8H2v-8h4a2 2 0 100-4H2z" fill="#fff"/><rect x="15" y="12" width="9" height="10" fill="#fff"/></svg></div>
  <div class="badge" style="color:var(--magenta)">4</div><div class="name">PLANS</div></div>
<div class="tile" style="left:505px;background:var(--orange)">
  <div class="ring"><svg width="32" height="26" viewBox="0 0 26 20"><circle cx="6" cy="6" r="3.5" fill="#fff"/><circle cx="20" cy="6" r="3.5" fill="#fff"/><circle cx="13" cy="8" r="4" fill="#fff"/><path d="M6 20c0-5 3-8 7-8s7 3 7 8zM0 17c0-4 3-6 6-6s4 1 4 2M26 17c0-4-3-6-6-6s-4 1-4 2" fill="#fff"/></svg></div>
  <div class="badge" style="color:var(--orange)">12</div><div class="name">CONTACTS</div></div>
<div class="tile" style="left:718px;background:var(--green)">
  <div class="ring"><svg width="26" height="26" viewBox="0 0 24 24"><path d="M2 3h14v19H2z" fill="none" stroke="#fff" stroke-width="1.8"/><path d="M5 8h8M5 12h6M5 16h5" stroke="#fff" stroke-width="1.6"/><path d="M22 4l-9 9-1 4 4-1 9-9z" fill="#fff"/></svg></div>
  <div class="badge" style="color:var(--green)">8</div><div class="name">DOCUMENTS</div></div>
<div class="tile" style="left:933px;background:var(--teal)">
  <div class="ring"><svg width="26" height="24" viewBox="0 0 24 22"><path d="M1 9l11-7 11 7v12H1z M1 9l11 7 11-7" fill="none" stroke="#fff" stroke-width="1.6"/><path d="M6 7h12M6 10h12" stroke="#fff" stroke-width="1.3"/></svg></div>
  <div class="badge" style="color:var(--teal)">12</div><div class="name">MESSAGES</div></div>

<h2 class="section-title">Recommended Plans</h2>
<div class="plan" style="left:316px"><div class="circ"><svg width="46" height="54" viewBox="0 0 46 54"><g fill="#2b9be0"><circle cx="12" cy="7" r="6"/><circle cx="32" cy="7" r="6"/><rect x="4" y="15" width="16" height="22" rx="3"/><rect x="24" y="15" width="16" height="22" rx="3"/><rect x="6" y="36" width="5" height="18"/><rect x="13" y="36" width="5" height="18"/><rect x="27" y="36" width="5" height="18"/><rect x="34" y="36" width="5" height="18"/><circle cx="6" cy="30" r="4"/><circle cx="40" cy="30" r="4"/><rect x="2" y="35" width="8" height="12"/><rect x="36" y="35" width="8" height="12"/></g></svg></div><div class="cap">Life</div></div>
<div class="plan" style="left:448px"><div class="circ"><svg width="40" height="50" viewBox="0 0 40 50"><g fill="#2b9be0"><circle cx="8" cy="8" r="5"/><path d="M12 14l10 8 12-4 2 4-14 6-4 8 12 10-3 3-15-12 4-10-8-7z"/></g><path d="M8 46q10 4 20 0" stroke="#2b9be0" stroke-width="1.5" fill="none"/></svg></div><div class="cap">Accident</div></div>
<div class="plan" style="left:589px"><div class="circ"><svg width="44" height="40" viewBox="0 0 44 40"><path d="M22 2L2 18h6v20h28V18h6z" fill="#2b9be0"/><g fill="#fff"><rect x="12" y="22" width="6" height="6"/><rect x="26" y="22" width="6" height="6"/><rect x="19" y="28" width="6" height="10"/></g></svg></div><div class="cap">Home</div></div>
<div class="plan" style="left:722px"><div class="circ"><svg width="48" height="38" viewBox="0 0 48 38"><path d="M8 14l5-11h22l5 11h4v14h-4v8h-7v-8H15v8H8v-8H4V14z" fill="#2b9be0"/><path d="M13 13l3-7h16l3 7z" fill="#fff"/><circle cx="11" cy="21" r="3" fill="#fff"/><circle cx="37" cy="21" r="3" fill="#fff"/><rect x="18" y="20" width="12" height="2" fill="#fff"/></svg></div><div class="cap">Auto</div></div>
<div class="plan" style="left:854px"><div class="circ"><svg width="46" height="46" viewBox="0 0 46 46"><circle cx="23" cy="26" r="17" fill="#2b9be0"/><path d="M6 26h34M23 9v34M10 17h26M10 35h26" stroke="#fff" stroke-width="2"/><ellipse cx="23" cy="26" rx="7" ry="17" fill="none" stroke="#fff" stroke-width="2"/><path d="M30 2l6 6 6-3-2 4 4 2-6 1-2 5-2-6z" fill="#2b9be0"/></svg></div><div class="cap">Travel</div></div>
<div class="plan" style="left:995px"><div class="circ"><svg width="36" height="36" viewBox="0 0 36 36"><path d="M18 2v32M2 18h32" stroke="#2b9be0" stroke-width="6"/></svg></div><div class="cap">More</div></div>

<section class="panel">
  <div class="panel-head"><h2>Active Plans</h2><span class="close">✕</span></div>
  <div class="row live" style="height:80px">
    <div class="tag" style="top:23px;background:var(--red);font-size:13px">END</div>
    <div class="title" style="top:21px">Outdoor Adventure - LIVE</div>
    <div class="meta" style="top:47px"><span>Start: 7/1/2015</span><span>End : 7/05/2015</span><span>Groups: 2</span><span>Documents: 0</span><span>Contacts: 4</span></div>
  </div>
  <div class="row" style="height:75px">
    <div class="title" style="top:19px">Angie A Birthday</div>
    <div class="meta" style="top:45px"><span>Start: 7/1/2015</span><span>End : 7/05/2015</span><span>Groups: 2</span><span>Documents: 0</span><span>Contacts: 4</span></div>
  </div>
  <div class="row" style="height:74px">
    <div class="title" style="top:17px">Maui Vacation</div>
    <div class="meta" style="top:43px"><span>Start: 7/1/2015</span><span>End : 7/05/2015</span><span>Groups: 2</span><span>Documents: 0</span><span>Contacts: 4</span></div>
  </div>
  <div class="row" style="height:78px">
    <div class="tag" style="top:20px;background:var(--lime);font-size:9.5px">START</div>
    <div class="title" style="top:18px">Having a Baby</div>
    <div class="meta" style="top:44px"><span>Start: 7/1/2015</span><span>End : 7/05/2015</span><span>Groups: 2</span><span>Documents: 0</span><span>Contacts: 4</span></div>
  </div>
</section>

<footer class="footer">
  <p>Copyright © 2015 Brellomar. All Rights Reserved.</p>
  <span class="code">C7</span>
</footer>
</body>
</html>
```